New business card and project proposal template, letterhead

Hello, I'm looking for a new business card and project proposal template to go with my new logo. project Proposals are sent to clients as a pdf document. my updated website is www.lanternvale-films.com. Looking for a look of a hollywood studio. Not a lot of dark colors , Red can be used as am acent, but not as a main. (see logo)

Target Market(s)

Communication departments, marketing managers.

Industry/Entity Type

Videography

Colors
ec1f27

Requirements
Must have
• logo,
• Brightwater Frames Inc.
• #300 - 845 North Elmcrest
• Vancouver BC V6K 3R8
• www.lanternvale-films.com
• morwen@lanternvale-films.com
• Direct: 604 219 4738
• vimeo.com/lanternvalefilms
• twitter: @lanternvalefx
Should not have
• clowns

```html
<!DOCTYPE html>
<html lang="en">
<head>
<meta charset="utf-8">
<title>Brightwater Frames – Business Card</title>
<link href="https://fonts.googleapis.com/css2?family=Roboto:wght@400;500;700&display=swap" rel="stylesheet">
<style>
  :root {
    --backdrop: #a9a7a7;
    --card-dark: #1c1c1e;
    --card-light: #f6f6f6;
    --ink: #231f20;
    --ink-soft: #333;
    --accent: #8e2433;
    --accent-deep: #6e1520;
    --accent-light: #a3323f;
    --white: #ffffff;
  }
  * { box-sizing: border-box; margin: 0; padding: 0; }
  html, body { width: 1200px; height: 1200px; overflow: hidden; }
  body {
    background: var(--backdrop);
    font-family: "Roboto", Arial, sans-serif;
    position: relative;
  }
  .card {
    position: absolute;
    width: 712px;
    height: 418px;
    border-radius: 22px;
    overflow: hidden;
  }
  .card--back { left: 238px; top: 118px; background: var(--card-dark); }
  .card--front { left: 231px; top: 644px; background: var(--card-light); }

  .wordmark {
    position: absolute;
    font-weight: 700;
    letter-spacing: 0.5px;
    white-space: nowrap;
    line-height: 1;
  }
  .wordmark__dot {
    display: inline-block;
    width: 0.42em; height: 0.42em;
    background: var(--accent);
    margin-left: 0.25em;
    vertical-align: 0.08em;
  }
  .tagline {
    position: absolute;
    font-weight: 400;
    white-space: nowrap;
    line-height: 1;
  }

  .card--back .wordmark { left: 66px; top: 176px; font-size: 44px; color: var(--white); }
  .card--back .tagline { right: 64px; top: 222px; font-size: 20px; color: var(--white); }

  .card--front .wordmark { left: 27px; top: 41px; font-size: 36px; color: var(--ink); }
  .card--front .tagline { left: 234px; top: 81px; font-size: 17px; color: var(--ink-soft); }

  .accent-panel {
    position: absolute;
    right: 0; top: 0;
    width: 145px; height: 100%;
    background: linear-gradient(180deg, var(--accent-deep), var(--accent-light));
  }

  .person { position: absolute; left: 28px; top: 171px; }
  .person__name {
    font-size: 25px; font-weight: 700; letter-spacing: 1.5px;
    color: var(--accent); line-height: 1;
  }
  .person__role { font-size: 15px; color: var(--ink); margin-top: 7px; }

  .contact {
    position: absolute; left: 28px; top: 263px;
    list-style: none; font-size: 16.5px; color: var(--ink);
  }
  .contact li { height: 24px; display: flex; align-items: center; }
  .contact li.address { margin-top: 3px; }
  .contact svg { width: 17px; height: 14px; margin-right: 9px; fill: var(--accent); flex: none; }
  .contact .plain-dot {
    width: 11px; height: 11px; border-radius: 50%;
    background: var(--accent); margin: 0 12px 0 3px; flex: none;
  }
  .contact .gap { display: inline-block; width: 6px; }
</style>
</head>
<body>

  <section class="card card--back" aria-label="Card back">
    <div class="wordmark">BRIGHTWATER FRAMES<span class="wordmark__dot"></span></div>
    <div class="tagline">crafting stories. framing motion.</div>
  </section>

  <section class="card card--front" aria-label="Card front">
    <div class="accent-panel"></div>
    <div class="wordmark">BRIGHTWATER FRAMES<span class="wordmark__dot"></span></div>
    <div class="tagline">crafting stories. framing motion.</div>

    <div class="person">
      <div class="person__name">MORWEN</div>
      <div class="person__role">Managing Director</div>
    </div>

    <ul class="contact">
      <li>
        <svg viewBox="0 0 17 14" aria-hidden="true"><path d="M1 5c0-2 3-3.5 7.5-3.5S16 3 16 5v1.5h-3.5V5h-8v1.5H1z"/><rect x="3" y="7" width="11" height="6" rx="1"/></svg>
        604 219 4738
      </li>
      <li>
        <svg viewBox="0 0 17 14" aria-hidden="true"><circle cx="8.5" cy="7" r="6" fill="none" style="stroke:var(--accent)" stroke-width="1.4"/><path d="M2.5 7h12M8.5 1c-3 3.5-3 8.5 0 12M8.5 1c3 3.5 3 8.5 0 12" fill="none" style="stroke:var(--accent)" stroke-width="1.2"/></svg>
        www.lanternvale-films.com
      </li>
      <li>
        <svg viewBox="0 0 17 14" aria-hidden="true"><rect x="0.5" y="1.5" width="16" height="11"/><path d="M1 2l7.5 6 7.5-6" fill="none" stroke="#f6f6f6" stroke-width="1.4"/></svg>
        morwen@lanternvale-films.com
      </li>
      <li>
        <span class="plain-dot"></span>/lanternvalefilms<span class="gap"></span><span class="plain-dot"></span>@lanternvalefx
      </li>
      <li class="address">#300 - 845 North Elmcrest Vancouver, BC</li>
    </ul>
  </section>

</body>
</html>
```